Spring Email Enticing Guest/Potential Guest to spend this Spring Break at The Lodge at Pelham...

Text - Amazing Spring Rates to Celebrate Being Ranked 14th Family Resort in the U.S. by Staymeter

- make the email very spring like with bold/warm colors

at bottom - New in 2019 enjoy Splashmoor Cove and New Phase 3 rooms
- the room pictures attached for New Phase 3 rooms and renditions are Splashmoor Cove (water play area)

Target Market(s)

Guest looking to book spring break

Industry/Entity Type

Hospitality

Requirements
Must have
• Phone: 800.555.0184
• Website: https://www.lodgeatpelhamhollow.com/
• Email will be sent via Mailbeacon Pro so must be formatted to be sent correctly

```html
<!DOCTYPE html>
<html lang="en">
<head>
<meta charset="utf-8">
<title>Spring Rates – The Lodge at Pelham Hollow</title>
<link href="https://fonts.googleapis.com/css2?family=Poppins:ital,wght@0,400;0,500;0,600;0,700;1,400&display=swap" rel="stylesheet">
<style>
  :root {
    --brand-blue: #2d6db6;
    --brand-blue-dark: #24579a;
    --sun-yellow: #f6b817;
    --sun-yellow-deep: #e9a90c;
    --warm-orange: #d8924a;
    --ink: #2f2f2f;
    --paper: #eaf2fa;
    --cream: #f4f1e6;
    --white: #ffffff;
  }
  * { box-sizing: border-box; margin: 0; padding: 0; }
  html, body { width: 691px; height: 1200px; overflow: hidden; }
  body { font-family: "Poppins", Arial, sans-serif; background: var(--paper); }
  .email { position: relative; width: 691px; height: 1200px; overflow: hidden; background: var(--paper); }

  .header { position: absolute; left: 0; top: 0; width: 691px; height: 110px; background: var(--cream); }
  .header-contact { position: absolute; right: 0; top: 0; width: 317px; height: 110px; background: var(--brand-blue);
    clip-path: polygon(10% 0, 100% 0, 100% 100%, 0 100%); }
  .brand { position: absolute; left: 44px; top: 30px; width: 160px; text-align: center;
    font-weight: 700; font-size: 19px; line-height: 24px; color: var(--brand-blue-dark); }
  .call-label { position: absolute; left: 432px; top: 22px; font-size: 21px; font-weight: 500; color: var(--white); }
  .call-number { position: absolute; left: 432px; top: 46px; font-size: 35px; font-weight: 600; color: var(--sun-yellow); letter-spacing: 0.3px; }

  .hero { position: absolute; left: 0; top: 110px; width: 691px; height: 331px;
    background: linear-gradient(100deg, #6f8fbf 0%, #3d4f92 35%, #2a3f86 55%, #c48a4a 75%, #e5a85a 100%); }
  .hero-band { position: absolute; left: 0; top: 110px; width: 691px; height: 6px; background: var(--brand-blue); }

  .badge { position: absolute; left: 20px; top: 202px; width: 289px; height: 328px; }
  .badge-text { position: absolute; left: 30px; top: 256px; width: 269px; text-align: center;
    color: var(--white); font-weight: 700; font-size: 23.5px; line-height: 32px; }

  .backdrop { position: absolute; left: 0; top: 441px; width: 691px; height: 759px;
    background: linear-gradient(180deg, #d7e3ef 0%, #e6eef7 25%, var(--paper) 60%, #eef4fa 100%); }

  .news-title { position: absolute; left: 0; top: 575px; width: 691px; text-align: center;
    font-size: 29px; font-weight: 400; color: var(--ink); }
  .news-sub { position: absolute; left: 0; top: 613px; width: 691px; text-align: center;
    font-size: 29px; font-weight: 400; color: var(--warm-orange); }
  .news-rule { position: absolute; left: 297px; top: 661px; width: 76px; height: 3px; background: var(--warm-orange); }

  .gallery-tile { position: absolute; top: 706px; width: 207px; height: 200px;
    border: 3px solid var(--sun-yellow); border-radius: 4px 18px 4px 18px; }
  .tile-splash { left: 21px; background: linear-gradient(160deg, #7fb0d8 0%, #5d8fbf 40%, #46a9c9 75%, #8cc9d9 100%); }
  .tile-bedroom { left: 241px; background: linear-gradient(160deg, #d8d9b8 0%, #c9c7a4 40%, #ecebe4 70%, #7f8a90 100%); }
  .tile-suite { left: 461px; background: linear-gradient(160deg, #cfc8b5 0%, #bcb3a0 40%, #5b5d63 70%, #8b9096 100%); }

  .info-box { position: absolute; left: 21px; top: 951px; width: 649px; height: 124px;
    background: var(--brand-blue); border-radius: 36px; text-align: center; color: var(--white); }
  .info-label { margin-top: 26px; font-size: 25px; font-weight: 400; }
  .info-url { margin-top: 2px; font-size: 27.5px; font-weight: 500; color: var(--sun-yellow); }

  .social { position: absolute; left: 258px; top: 1060px; width: 176px; height: 36px; display: flex; justify-content: space-between; }
  .social-dot { width: 36px; height: 36px; border-radius: 50%; background: var(--white); border: 2px solid var(--brand-blue); }

  .copyright { position: absolute; left: 0; top: 1133px; width: 691px; text-align: center; font-size: 15px; color: var(--ink); }
  .unsubscribe { position: absolute; left: 0; top: 1158px; width: 691px; text-align: center;
    font-size: 15px; font-style: italic; color: var(--brand-blue); text-decoration: underline; }
</style>
</head>
<body>
<div class="email">
  <header>
    <div class="header"></div>
    <div class="brand">The Lodge at Pelham Hollow</div>
    <div class="header-contact"></div>
    <div class="call-label">Call Us:</div>
    <div class="call-number">800.555.0184</div>
  </header>

  <div class="hero" role="img" aria-label="Dusk photo of the multi-storey lodge building with lit windows"></div>
  <div class="hero-band"></div>

  <svg class="badge" viewBox="0 0 289 328" aria-hidden="true">
    <path d="M8 0 H281 Q289 0 289 8 V232 L144.5 328 L0 232 V8 Q0 0 8 0 Z" fill="var(--sun-yellow)"/>
    <path d="M14 8 H275 Q281 8 281 14 V227 L144.5 317 L8 227 V14 Q8 8 14 8 Z" fill="none" stroke="#fbd873" stroke-width="1.5"/>
  </svg>
  <p class="badge-text">Amazing Spring Rates to Celebrate Being Ranked 14th Family Resort in the U.S. by Staymeter</p>

  <div class="backdrop" role="img" aria-label="Faded view of colourful water slides"></div>

  <h2 class="news-title">New in 2019 enjoy Splashmoor Cove &amp;</h2>
  <h3 class="news-sub">New Phase 3 rooms</h3>
  <div class="news-rule"></div>

  <div class="gallery-tile tile-splash" role="img" aria-label="Guests relaxing on a pool float at Splashmoor Cove"></div>
  <div class="gallery-tile tile-bedroom" role="img" aria-label="New Phase 3 bedroom with a made bed and lamps"></div>
  <div class="gallery-tile tile-suite" role="img" aria-label="New Phase 3 suite kitchen and dining table"></div>

  <div class="info-box">
    <p class="info-label">For More Information Visit</p>
    <p class="info-url">www.lodgeatpelhamhollow.com</p>
  </div>

  <div class="social" aria-label="Social links">
    <span class="social-dot"></span><span class="social-dot"></span><span class="social-dot"></span><span class="social-dot"></span>
  </div>

  <footer>
    <p class="copyright">Copyright @ 2019 lodgeatpelhamhollow</p>
    <p class="unsubscribe">Unscribe with us</p>
  </footer>
</div>
</body>
</html>
```